Accounting services

Looking for a Business card & Logo design

company name - LUMEN ACCOUNTING & TAXATION SOLUTIONS

name - Corwin Pell

position - Accountant / Business Consultant

email - "undecided"

Tel : (868) 512-4873 / (868) 587-2196

**PUT THESE TO THE BACK**
Accounting - VAT * INCOME/CORP TAX * RETURNS

REGISTRATION - VAT * NIS * Company Registration/Business Plan

Industry/Entity Type

Business

```html
<!DOCTYPE html>
<html lang="en">
<head>
<meta charset="utf-8">
<title>Lumen Accounting &amp; Taxation Solutions – Business Card</title>
<link href="https://fonts.googleapis.com/css2?family=Saira:wght@400;500;700&family=Archivo:wght@500&display=swap" rel="stylesheet">
<style>
  :root {
    --page: #ffffff;
    --navy: #1f3f86;
    --blue-deep: #1c4a8e;
    --blue-mid: #2a74b4;
    --blue-light: #2b9bd0;
    --silver-light: #fbfbfb;
    --silver-mid: #e3e4e6;
    --silver-dark: #b9bcc0;
    --ink: #2c4a8c;
    --white: #ffffff;
  }
  * { margin: 0; padding: 0; box-sizing: border-box; }
  html, body {
    width: 1058px; height: 1200px; overflow: hidden;
    background: var(--page);
  }
  .canvas { position: relative; width: 1058px; height: 1200px; }

  .card {
    position: absolute;
    width: 780px; height: 457px;
    overflow: hidden;
    box-shadow: 6px 8px 14px rgba(0,0,0,0.22);
    font-family: "Saira", sans-serif;
  }
  .card--front { left: 122px; top: 114px; }
  .card--back  { left: 124px; top: 620px; }
  .card__bg { position: absolute; inset: 0; width: 100%; height: 100%; }

  /* wordmark */
  .wordmark {
    position: absolute; left: 0; right: 0;
    display: flex; justify-content: center; align-items: center; gap: 16px;
  }
  .wordmark__square { width: 58px; height: 58px; background: var(--blue-deep); }
  .wordmark__name {
    font-family: "Saira", sans-serif; font-weight: 500;
    line-height: 1.02; letter-spacing: 0.5px;
  }
  .card--front .wordmark { top: 50px; }
  .card--front .wordmark__name { color: var(--navy); font-size: 27px; }
  .card--back .wordmark { top: 42px; gap: 12px; }
  .card--back .wordmark__square { width: 46px; height: 46px; background: var(--white); }
  .card--back .wordmark__name { color: var(--white); font-size: 21px; }

  /* front details */
  .person {
    position: absolute; left: 0; right: 0; top: 212px;
    text-align: center; color: var(--white);
  }
  .person__name { font-weight: 700; font-size: 25px; line-height: 1.2; letter-spacing: 0.5px; }
  .person__role { font-weight: 400; font-size: 24px; line-height: 1.3; letter-spacing: 0.6px; }

  .contacts {
    position: absolute; left: 226px; top: 287px;
    list-style: none; color: var(--white);
    font-size: 25px; letter-spacing: 0.8px;
  }
  .contacts li { display: flex; align-items: center; height: 37px; }
  .contacts .icon { width: 24px; height: 24px; margin-right: 12px; flex: none; }
  .contacts .phones { height: 74px; }
  .contacts .phones span { display: block; line-height: 37px; }
  .contacts .web { margin-top: 2px; }

  /* back services */
  .services {
    position: absolute; left: 0; right: 0; top: 205px;
    text-align: center; color: var(--ink);
    font-family: "Archivo", sans-serif; font-weight: 500;
  }
  .services__title { font-size: 24px; line-height: 34px; letter-spacing: -0.3px; }
  .services__list { font-size: 24px; line-height: 38px; letter-spacing: 0.2px; }
  .services__group + .services__group { margin-top: 39px; }
</style>
</head>
<body>
<main class="canvas">

  <section class="card card--front" aria-label="Business card front">
    <svg class="card__bg" viewBox="0 0 780 457" preserveAspectRatio="none" aria-hidden="true">
      <defs>
        <linearGradient id="frontSilver" x1="0" x2="1" y1="0" y2="0">
          <stop offset="0" stop-color="#cfd1d4"/>
          <stop offset="0.45" stop-color="#ffffff"/>
          <stop offset="0.7" stop-color="#f4f4f5"/>
          <stop offset="1" stop-color="#c6c8cb"/>
        </linearGradient>
        <linearGradient id="frontBlue" x1="0" x2="0" y1="0" y2="1">
          <stop offset="0" stop-color="#2ba0d4"/>
          <stop offset="0.45" stop-color="#1d62a4"/>
          <stop offset="0.75" stop-color="#1b4a8f"/>
          <stop offset="1" stop-color="#2a5fa6"/>
        </linearGradient>
        <linearGradient id="frontEdge" x1="0" x2="1">
          <stop offset="0" stop-color="#9da1a6"/>
          <stop offset="0.5" stop-color="#f2f2f3"/>
          <stop offset="1" stop-color="#9da1a6"/>
        </linearGradient>
      </defs>
      <rect width="780" height="457" fill="url(#frontSilver)"/>
      <path d="M0 198 Q390 152 780 200 L780 457 L0 457 Z" fill="url(#frontEdge)"/>
      <path d="M0 207 Q390 164 780 208 L780 457 L0 457 Z" fill="url(#frontBlue)"/>
    </svg>

    <div class="wordmark">
      <span class="wordmark__square"></span>
      <p class="wordmark__name">LUMEN ACCOUNTING<br>&amp; TAXATION SOLUTIONS</p>
    </div>

    <div class="person">
      <h1 class="person__name">Corwin Pell</h1>
      <p class="person__role">Accountant/Business Consultant</p>
    </div>

    <ul class="contacts">
      <li class="phones">
        <svg class="icon" viewBox="0 0 24 24" aria-hidden="true"><path d="M6 3c1.2-.6 2 .1 2.6 1.2l1.3 2.6c.5 1 .2 1.8-.6 2.4l-1 .7c.8 2.6 2.4 4.6 4.6 6.1l1-.8c.8-.6 1.6-.6 2.4 0l2.4 1.7c1 .7 1.1 1.6.4 2.6-1.2 1.5-2.8 2-4.6 1.2C9 18.4 5.3 14 3.7 8.3 3.1 6 4.2 4 6 3z" fill="#fff"/></svg>
        <div><span>(868) 512-4873</span><span>(868) 587-2196</span></div>
      </li>
      <li>
        <svg class="icon" viewBox="0 0 24 24" aria-hidden="true"><rect x="2.5" y="6" width="19" height="13" fill="none" stroke="#fff" stroke-width="1.8"/><path d="M2.5 6l9.5 7.5L21.5 6M2.5 19l7-6M21.5 19l-7-6" fill="none" stroke="#fff" stroke-width="1.6"/></svg>
        <span>corwin@lumensolutions.com</span>
      </li>
      <li class="web">
        <svg class="icon" viewBox="0 0 24 24" aria-hidden="true"><g fill="none" stroke="#fff" stroke-width="1.5"><circle cx="12" cy="12" r="9.5"/><ellipse cx="12" cy="12" rx="4.5" ry="9.5"/><path d="M2.5 12h19M4 7h16M4 17h16M12 2.5v19"/></g></svg>
        <span>www.lumensolutions.com</span>
      </li>
    </ul>
  </section>

  <section class="card card--back" aria-label="Business card back">
    <svg class="card__bg" viewBox="0 0 781 457" preserveAspectRatio="none" aria-hidden="true">
      <defs>
        <linearGradient id="backSilver" x1="0" x2="1" y1="0" y2="0">
          <stop offset="0" stop-color="#cdcfd2"/>
          <stop offset="0.4" stop-color="#ffffff"/>
          <stop offset="0.7" stop-color="#f6f6f7"/>
          <stop offset="1" stop-color="#c9cbce"/>
        </linearGradient>
        <linearGradient id="backBlue" x1="0" x2="0" y1="0" y2="1">
          <stop offset="0" stop-color="#1f3f86"/>
          <stop offset="0.5" stop-color="#1c5fa2"/>
          <stop offset="1" stop-color="#2aa3d6"/>
        </linearGradient>
        <linearGradient id="backEdge" x1="0" x2="1">
          <stop offset="0" stop-color="#a0a4a9"/>
          <stop offset="0.5" stop-color="#f2f2f3"/>
          <stop offset="1" stop-color="#a0a4a9"/>
        </linearGradient>
      </defs>
      <rect width="781" height="457" fill="url(#backSilver)"/>
      <path d="M0 0 H781 V142 Q390 170 0 138 Z" fill="url(#backEdge)"/>
      <path d="M0 0 H781 V128 Q390 158 0 128 Z" fill="url(#backBlue)"/>
    </svg>

    <div class="wordmark">
      <span class="wordmark__square"></span>
      <p class="wordmark__name">LUMEN ACCOUNTING<br>&amp; TAXATION SOLUTIONS</p>
    </div>

    <div class="services">
      <div class="services__group">
        <h2 class="services__title">ACCOUNTING</h2>
        <p class="services__list">VAT &nbsp;•&nbsp; INCOME/CORP TAX &nbsp;•&nbsp; RETURNS</p>
      </div>
      <div class="services__group">
        <h2 class="services__title">REGISTRATION</h2>
        <p class="services__list">VAT • NIS • COMPANY REGISTRATION / BUSINESS PLAN</p>
      </div>
    </div>
  </section>

</main>
</body>
</html>
```